Online interactive tutorial for year 2 to year 12 students in Australia

Website design for a new online tutorial for year 2 to year 12 students in Australia.

- The tutorial will be conducted via live webcam and within a dedicated interactive space
- The tutorial will be provided by high scoring undergraduates studying in top Australian universities.
- The tutors will be going through interviews & assessments & only top students are allowed to apply.
- Parents will do search and select tutor and have short 15 mins video interaction with potential tutors before booking them for their children for tutoring.
- hourly cost of booking (no monthly subscription or no hour limits)
- Tutors will have their own profile

Please see the attached for detailed page functionality.

The look and feel of the design must consider the following:
- must be educational but not dull and should stand out
- must appeal to younger generation - tutees (8-18 years), tutors (19-25), parents (30-50).
- Ideas for Logos (brivano.com.au but not confirmed)

Target Market(s)

tutees (8-18 years), tutors (19-25 years), parents (30-50 years).

Industry/Entity Type

Education

Coding

Coded - Design and coding required

Number of Pages Required

5+ page

Font styles to use
Serif

Requirements
Must have
• The look and feel of the design must consider the following:
• - must be educational but not dull and should stand out
• - must appeal to younger generation - tutees (8-18 years), tutors (19-25), parents (30-50).
Should not have
• Dullness

```html
<!DOCTYPE html>
<html lang="en">
<head>
<meta charset="utf-8">
<title>Brivano – Online Training</title>
<link href="https://fonts.googleapis.com/css2?family=Roboto:wght@400;500;700&family=Oswald:wght@500&display=swap" rel="stylesheet">
<style>
:root{
  --blue:#1b8fc6;
  --blue-dark:#1479ab;
  --blue-deep:#3553b5;
  --blue-cal:#2f9de0;
  --ink:#222;
  --text:#666;
  --light:#f1f2f4;
  --dark:#2a2a2a;
  --black:#121212;
  --white:#fff;
}
*{box-sizing:border-box;margin:0;padding:0}
html,body{width:1200px;height:3191px;overflow:hidden}
body{font-family:"Roboto",Arial,sans-serif;color:var(--ink);background:var(--white);position:relative}
section,header,footer,.topbar,.bottom{position:absolute;left:0;width:1200px}
.topbar{top:0;height:43px;background:var(--blue);color:var(--white);font-size:13px;display:flex;align-items:center;justify-content:space-between;padding:0 85px}
.topbar .contact span{margin-left:26px}
.site-header{top:43px;height:95px;display:flex;align-items:center;justify-content:space-between;padding:0 85px;box-shadow:0 2px 4px rgba(0,0,0,.08)}
.brand{font-weight:700;font-size:34px;color:var(--blue);letter-spacing:1px}
.nav{display:flex;align-items:center;gap:34px;font-size:15px;color:#333}
.nav .active{color:var(--blue)}
.nav .search{width:30px;height:30px;border:1px solid #ddd;display:flex;align-items:center;justify-content:center}
.hero{top:138px;height:552px;background:linear-gradient(135deg,#5d6f7e,#a88f7e 40%,#7d8fa2 70%,#465663)}
.hero h1{position:absolute;left:88px;top:384px;font-family:"Oswald",sans-serif;font-weight:500;font-size:52px;color:var(--white);line-height:1}
.hero p{position:absolute;left:88px;top:440px;font-family:"Oswald",sans-serif;font-size:32px;color:var(--white)}
.hero .arrows{position:absolute;right:85px;top:442px;display:flex;gap:8px}
.hero .arrows span{width:32px;height:32px;border-radius:50%;background:rgba(0,0,0,.55);display:flex;align-items:center;justify-content:center}
.welcome{top:690px;height:218px;text-align:center}
.sec-title{font-size:25px;font-weight:500;letter-spacing:.5px;color:var(--ink)}
.sec-title em{font-style:normal;color:var(--blue)}
.welcome .sec-title{margin-top:52px}
.welcome p{width:1020px;margin:22px auto 0;font-size:12.5px;line-height:21px;color:var(--text)}
.services{top:908px;height:441px;background:linear-gradient(rgba(27,143,198,.9),rgba(20,121,171,.92)),linear-gradient(120deg,#6fa9c9,#2d7fae);color:var(--white);text-align:center}
.services .sec-title{color:var(--white);margin-top:55px}
.service{position:absolute;top:133px;width:230px;margin-left:-115px}
.service .icon{width:106px;height:106px;border-radius:50%;background:var(--white);margin:0 auto;display:flex;align-items:center;justify-content:center}
.service h3{margin-top:26px;font-size:17px;font-weight:500;line-height:25px}
.service p{margin-top:12px;font-size:12px;line-height:20px;opacity:.9}
.videos{top:1349px;height:456px;text-align:center}
.videos .sec-title{margin-top:50px}
.video-card{position:absolute;top:111px;width:317px;text-align:left}
.video-card .thumb{height:193px;border:4px solid #e5e5e5;position:relative;background:linear-gradient(135deg,#c9a27e,#e8d8c4 50%,#8fa7b8)}
.video-card .thumb .play{position:absolute;left:50%;top:50%;width:58px;height:58px;margin:-29px;border-radius:50%;background:rgba(0,0,0,.55);display:flex;align-items:center;justify-content:center}
.video-card h3{margin-top:20px;font-size:15px;font-weight:500;color:#333}
.video-card p{margin-top:10px;font-size:12px;line-height:20px;color:var(--text)}
.video-card a{display:block;margin-top:8px;font-size:12px;color:var(--blue);text-decoration:none}
.profile{top:1805px;height:385px;background:linear-gradient(135deg,#f5f6f8,#e9ebee 50%,#f7f8f9);text-align:center}
.profile .sec-title{margin-top:48px}
.avatar{border-radius:50%;border:4px solid var(--white);box-shadow:0 1px 4px rgba(0,0,0,.25);background:radial-gradient(circle at 50% 40%,#d9b197,#8a6a55 70%,#5a4a40)}
.profile .avatar{width:94px;height:94px;margin:25px auto 0}
.profile blockquote{width:900px;margin:36px auto 0;font-size:12px;line-height:20px;color:var(--text)}
.profile blockquote b{color:var(--blue)}
.profile cite{display:block;margin-top:14px;color:var(--blue);font-size:15px}
.apply{top:2190px;height:296px;background:linear-gradient(rgba(20,20,20,.82),rgba(20,20,20,.82)),linear-gradient(120deg,#6b5b4c,#33404a);color:var(--white);text-align:center}
.apply h2{margin-top:70px;font-size:31px;font-weight:500}
.apply p{width:760px;margin:18px auto 0;font-size:17px;line-height:28px}
.apply .btn{display:inline-block;margin-top:28px;padding:8px 24px;border:1px solid var(--white);border-radius:20px;font-size:15px}
.schedule{top:2486px;height:402px}
.schedule .sec-title{position:absolute;left:372px;top:40px;font-size:21px}
.schedule .nav-arrows{position:absolute;right:85px;top:42px}
.calendar{position:absolute;left:85px;top:87px;width:273px;color:var(--white);font-size:12px}
.calendar .month{height:43px;background:var(--blue-deep);display:flex;align-items:center;justify-content:space-between;padding:0 14px;font-size:13px}
.calendar table{width:100%;border-collapse:collapse;table-layout:fixed}
.calendar td,.calendar th{height:33px;text-align:center;border:1px solid rgba(255,255,255,.35);background:var(--blue-deep);font-weight:400}
.calendar th{background:var(--blue-cal);font-weight:500}
.calendar td.today{background:#1c1c2a}
.calendar td.empty{background:var(--white);border-color:var(--white)}
.tutor{position:absolute;top:87px;width:234px;height:266px;background:var(--white);box-shadow:0 1px 6px rgba(0,0,0,.2);text-align:center}
.tutor .avatar{width:126px;height:126px;margin:12px auto 0}
.tutor h4{margin-top:20px;font-size:12px;font-weight:400;color:var(--blue)}
.tutor p{margin:8px 22px 0;font-size:11px;line-height:18px;color:var(--text)}
.tutor .btn{display:inline-block;margin-top:8px;width:104px;height:24px;line-height:24px;background:var(--blue-dark);color:var(--white);font-size:12px;border-radius:2px}
.site-footer{top:2888px;height:225px;background:var(--blue);color:var(--white);font-size:12px}
.site-footer h5{font-size:15px;font-weight:500;letter-spacing:.5px;margin-bottom:18px}
.col{position:absolute;top:43px}
.form-grid{display:grid;grid-template-columns:132px 132px;gap:6px 5px}
.form-grid div{height:28px;background:var(--white);color:#555;font-size:10px;padding:8px 6px}
.form-grid .wide{grid-column:1/3}
.send{display:inline-block;margin-top:8px;background:var(--black);padding:6px 18px;font-size:11px}
.links li{list-style:none;line-height:21px}
.links li::before{content:"› ";}
.touch p{line-height:21px;margin-bottom:14px}
.news p{width:210px;line-height:17px}
.news .sub{display:flex;margin-top:14px}
.news .sub span{width:140px;height:30px;background:var(--white);color:#999;font-size:10px;padding:9px 8px}
.news .sub b{width:63px;height:30px;background:var(--black);font-weight:400;font-size:11px;line-height:30px;text-align:center}
.social{display:flex;gap:16px;margin-top:16px}
.social span{width:32px;height:32px;border:1px solid var(--white);border-radius:50%}
.bottom{top:3113px;height:78px;background:var(--black);color:var(--white);font-size:12px;text-align:center;line-height:78px}
</style>
</head>
<body>
<div class="topbar">
  <div>TUTOR REGISTRATION &nbsp;|&nbsp; PARENT REGISTRATION &nbsp;|&nbsp; STUDENT LOG-INS</div>
  <div class="contact"><span>☎ +61-2-5550-1842</span><span>✉ : hello@brivano-mail.com</span></div>
</div>
<header class="site-header">
  <div class="brand">BRIVANO</div>
  <nav class="nav">
    <span class="active">HOME</span><span>ABOUT US</span><span>SCHEDULER</span><span>SERVICES</span><span>BLOG</span><span>CONTACT US</span>
    <span class="search"><svg width="12" height="12" viewBox="0 0 12 12"><circle cx="5" cy="5" r="3.6" fill="none" stroke="#555" stroke-width="1.4"/><line x1="7.6" y1="7.6" x2="11" y2="11" stroke="#555" stroke-width="1.4"/></svg></span>
  </nav>
</header>
<section class="hero" role="img" aria-label="Photo of smiling children gathered around a tablet">
  <h1>BRIVANO ONLINE TRAINING</h1>
  <p>Tutorial will be conducted via live webcam</p>
  <div class="arrows">
    <span><svg width="10" height="12" viewBox="0 0 10 12"><path d="M7 1 2 6l5 5" fill="none" stroke="#fff" stroke-width="2"/></svg></span>
    <span><svg width="10" height="12" viewBox="0 0 10 12"><path d="m3 1 5 5-5 5" fill="none" stroke="#fff" stroke-width="2"/></svg></span>
  </div>
</section>
<section class="welcome">
  <h2 class="sec-title">WELCOME TO &nbsp;<em>BRIVANO</em></h2>
  <p>Lorem Ipsum has been the industry's standard dummy text ever since the 1500s, when an unknown printer took a galley of type and scrambled it to make a type specimen book. It has survived not only five centuries, but also the leap into electronic typesetting, remaining essentially unchanged. It was popularised in the 1960s with the release of transfer sheets containing Lorem Ipsum passages, and more recently with desktop publishing software like common page layout tools including versions of Lorem Ipsum.</p>
</section>
<section class="services">
  <h2 class="sec-title">OUR SERVICES</h2>
  <div class="service" style="left:206px">
    <div class="icon"><svg width="44" height="30" viewBox="0 0 44 30"><rect x="0" y="2" width="28" height="26" rx="3" fill="#1b8fc6"/><path d="M30 11 44 2v26l-14-9z" fill="#1b8fc6"/></svg></div>
    <h3>CONDUCTED VIA<br>LIVE WEBCAM</h3>
    <p>Neque porro quisquam est qui dolor-<br>em ipsum quia dolor sit amet, con-</p>
  </div>
  <div class="service" style="left:470px">
    <div class="icon"><svg width="36" height="40" viewBox="0 0 36 40"><path d="M8 2h26v30H8a5 5 0 0 0 0 6h26" fill="none" stroke="#1b8fc6" stroke-width="4"/><path d="M8 2a5 5 0 0 0-5 5v26" fill="none" stroke="#1b8fc6" stroke-width="4"/><line x1="14" y1="11" x2="28" y2="11" stroke="#1b8fc6" stroke-width="3"/><line x1="14" y1="18" x2="28" y2="18" stroke="#1b8fc6" stroke-width="3"/></svg></div>
    <h3>HIGH SCORING<br>UNDERGRADUATES</h3>
    <p>Neque porro quisquam est qui dolor-<br>em ipsum quia dolor sit amet, con-</p>
  </div>
  <div class="service" style="left:734px">
    <div class="icon"><svg width="34" height="38" viewBox="0 0 34 38"><circle cx="17" cy="10" r="9" fill="#1b8fc6"/><path d="M0 38c0-11 7-16 17-16s17 5 17 16z" fill="#1b8fc6"/></svg></div>
    <h3>INTERVIEWS &amp;<br>ASSESSMENTS</h3>
    <p>Neque porro quisquam est qui dolor-<br>em ipsum quia dolor sit amet, con-</p>
  </div>
  <div class="service" style="left:996px">
    <div class="icon"><svg width="44" height="38" viewBox="0 0 44 38"><rect x="2" y="2" width="40" height="26" rx="2" fill="none" stroke="#1b8fc6" stroke-width="4"/><rect x="18" y="28" width="8" height="6" fill="#1b8fc6"/><rect x="10" y="34" width="24" height="4" fill="#1b8fc6"/></svg></div>
    <h3>HOURLY COST<br>OF BOOKING</h3>
    <p>Neque porro quisquam est qui dolor-<br>em ipsum quia dolor sit amet, con-</p>
  </div>
</section>
<section class="videos">
  <h2 class="sec-title">VIDEO OF <em>HOW IT WORKS</em></h2>
  <article class="video-card" style="left:85px">
    <div class="thumb" role="img" aria-label="Video still of a tutor reading with a young girl"><span class="play"><svg width="20" height="22" viewBox="0 0 20 22"><path d="M2 1v20l17-10z" fill="#fff"/></svg></span></div>
    <h3>NEQUE PORRO QUISQUAM EST QUI</h3>
    <p>Lorem ipsum dolor sit amet, consectetur adipiscing elit. Sed blandit massa vel mauris sollicitudin dignissim. Lorem ipsum</p>
    <a>Read More »</a>
  </article>
  <article class="video-card" style="left:438px">
    <div class="thumb" role="img" aria-label="Video still of two boys studying at a desk" style="background:linear-gradient(135deg,#c9a13a,#e2c46a 45%,#3d6fb2)"><span class="play"><svg width="20" height="22" viewBox="0 0 20 22"><path d="M2 1v20l17-10z" fill="#fff"/></svg></span></div>
    <h3>NEQUE PORRO QUISQUAM EST QUI</h3>
    <p>Lorem ipsum dolor sit amet, consectetur adipiscing elit. Sed blandit massa vel mauris sollicitudin dignissim. Lorem ipsum</p>
    <a>Read More »</a>
  </article>
  <article class="video-card" style="left:792px">
    <div class="thumb" role="img" aria-label="Video still of a father and son using a laptop" style="background:linear-gradient(135deg,#6a5a4a,#b9a58e 50%,#d8d2c6)"><span class="play"><svg width="20" height="22" viewBox="0 0 20 22"><path d="M2 1v20l17-10z" fill="#fff"/></svg></span></div>
    <h3>NEQUE PORRO QUISQUAM EST QUI</h3>
    <p>Lorem ipsum dolor sit amet, consectetur adipiscing elit. Sed blandit massa vel mauris sollicitudin dignissim. Lorem ipsum</p>
    <a>Read More »</a>
  </article>
</section>
<section class="profile">
  <h2 class="sec-title">TUTORS <em>PROFILE</em></h2>
  <div class="avatar" role="img" aria-label="Tutor portrait"></div>
  <blockquote><b>❝</b> &nbsp;Lorem Ipsum has been the industry's standard dummy text ever since the 1500s, when an unknown printer took a galley of type and scrambled it to make a type specimen book. It has survived not only five centuries, but also the leap into electronic typesetting, remaining essentially unchanged. It was popularised in the 1960s with the release of transfer sheets containing Lorem Ipsum passages, and more recently with desktop publishing software &nbsp;<b>❞</b>
    <cite>Neque porro quisquam est</cite>
  </blockquote>
</section>
<section class="apply" aria-label="Online training tutor">
  <h2>ONLINE TRAINING TUTOR</h2>
  <p>Lorem Ipsum has been the industry's standard dummy text ever since the 1500s, when an unknown printer took a galley of type and scrambled it to make a type specimen book.</p>
  <span class="btn">Apply Now</span>
</section>
<section class="schedule">
  <h2 class="sec-title">SCHEDULE</h2>
  <svg class="nav-arrows" width="26" height="14" viewBox="0 0 26 14"><path d="M7 1 2 7l5 6M19 1l5 6-5 6" fill="none" stroke="#222" stroke-width="2"/></svg>
  <div class="calendar">
    <div class="month"><span>‹</span><span>APRIL 2016</span><span>›</span></div>
    <table>
      <tr><th>M</th><th>T</th><th>W</th><th>T</th><th>F</th><th>S</th><th>S</th></tr>
      <tr><td>1</td><td>2</td><td>3</td><td>4</td><td>5</td><td>6</td><td>7</td></tr>
      <tr><td>8</td><td>9</td><td>10</td><td>11</td><td>12</td><td>13</td><td>14</td></tr>
      <tr><td>15</td><td>16</td><td>17</td><td>18</td><td>19</td><td class="today">20</td><td>21</td></tr>
      <tr><td>22</td><td>23</td><td>24</td><td>25</td><td>26</td><td>27</td><td>28</td></tr>
      <tr><td>29</td><td>30</td><td class="empty"></td><td class="empty"></td><td class="empty"></td><td class="empty"></td><td class="empty"></td></tr>
    </table>
  </div>
  <div class="tutor" style="left:372px">
    <div class="avatar" role="img" aria-label="Tutor portrait"></div>
    <h4>Neque porro quisquam</h4>
    <p>Lorem Ipsum has been the industry's standard dummy text ever since the</p>
    <span class="btn">Available</span>
  </div>
  <div class="tutor" style="left:619px">
    <div class="avatar" role="img" aria-label="Tutor portrait" style="background:radial-gradient(circle at 50% 40%,#e2b89c,#7a4a36 70%,#4a2e22)"></div>
    <h4>Neque porro quisquam</h4>
    <p>Lorem Ipsum has been the industry's standard dummy text ever since the</p>
    <span class="btn">Available</span>
  </div>
  <div class="tutor" style="left:868px">
    <div class="avatar" role="img" aria-label="Tutor portrait" style="background:radial-gradient(circle at 50% 40%,#e4c0a4,#9a7458 70%,#5e4838)"></div>
    <h4>Neque porro quisquam</h4>
    <p>Lorem Ipsum has been the industry's standard dummy text ever since the</p>
    <span class="btn">Available</span>
  </div>
</section>
<footer class="site-footer">
  <div class="col" style="left:89px">
    <h5>CONTACT FORM</h5>
    <div class="form-grid">
      <div>Name</div><div>Company info</div>
      <div>Phone</div><div>Email</div>
      <div class="wide">Message</div>
    </div>
    <span class="send">SEND</span>
  </div>
  <div class="col links" style="left:460px">
    <h5>LINKS</h5>
    <ul><li>About</li><li>Services</li><li>Tutor Registration</li><li>Parent Registration</li><li>Student Log-ins</li></ul>
  </div>
  <div class="col touch" style="left:653px">
    <h5>GET IN TOUCH</h5>
    <p>Address : 48 Carrow Lane,<br>Glenfield, NSW</p>
    <p>Phone : 02 5550 7719</p>
    <p>Email : hello@brivano-mail.com</p>
  </div>
  <div class="col news" style="left:904px">
    <h5>NEWSLETTER</h5>
    <p>Your about us information would fit here nicely.</p>
    <div class="sub"><span>Email address</span><b>Submit</b></div>
    <div class="social"><span></span><span></span><span></span></div>
  </div>
</footer>
<div class="bottom">Copyright © 2016. All Rights Reserved</div>
</body>
</html>
```